Business Card and Letterhead Design Project

I am starting my own building design business in Melbourne. The business will use my experience to help people make balanced life choices for building and renovating. My target audience is women -particularly mothers. I aim to be approachable and economical. I would like to see a design that uses greens or blues - natural colours. A lot of my work balances design and construction management so design should be flexible.

I want a double sided business card design and a letterhead design that I can use on all office correspondance

Design should have a clean crisp feel - a bit edgey in a feminine way.

Target Market(s)

Potential clients.

Industry/Entity Type

Construction

Requirements
Must have
• Brackenridge Design Studio
Harriet Oakley B.Arch

0497 283 541
harriet@brackenridgedesignstudio.example.au

14 Pembury Road
Larkmoor East VIC 3999
brackenridgedesignstudio.example.au
Nice to have
• Should have a calming feel to make me seem approachable but still professional.
Should not have
• No photos on the card or building plans.

```html
<!DOCTYPE html>
<html lang="en">
<head>
<meta charset="utf-8">
<title>Brackenridge Design Studio – Stationery</title>
<link rel="stylesheet" href="https://fonts.googleapis.com/css2?family=Questrial&display=swap">
<style>
  :root {
    --backdrop: #262626;
    --pool: #7eacbf;
    --pool-deep: #6f9fb3;
    --beige: #bdb8b2;
    --ink-grey: #9c9890;
    --paper: #ffffff;
    --paper-shade: #eceef0;
    --text-dark: #555;
    --text-blue: #5f9ab1;
  }
  * { box-sizing: border-box; margin: 0; padding: 0; }
  html, body { width: 1200px; height: 900px; overflow: hidden; }
  body {
    position: relative;
    background: var(--backdrop);
    font-family: "Questrial", "Century Gothic", sans-serif;
  }
  .piece { position: absolute; }

  /* Folder */
  .folder {
    left: 90px; top: 170px; width: 390px; height: 620px;
    background: var(--pool);
  }
  .folder-label {
    position: absolute; left: 0; top: 255px; width: 236px; height: 140px;
    background: linear-gradient(180deg, var(--paper), var(--paper-shade));
    display: flex; flex-direction: column; align-items: center; justify-content: center;
  }
  .folder-dots {
    position: absolute; left: 35px; top: 417px; display: flex; gap: 33px;
  }
  .folder-dots span { width: 5px; height: 5px; border-radius: 50%; background: #e3eef3; }

  /* Wordmark */
  .wordmark { color: var(--ink-grey); text-align: center; line-height: 1; }
  .wordmark .name { display: block; font-size: 30px; }
  .wordmark .sub { display: block; font-size: 10px; letter-spacing: 3px; margin-top: 6px; }
  .wordmark.small .name { font-size: 19px; }
  .wordmark.small .sub { font-size: 7px; letter-spacing: 2px; margin-top: 4px; }

  /* Letterhead */
  .letterhead {
    left: 506px; top: 190px; width: 410px; height: 575px;
    background: linear-gradient(180deg, var(--paper) 40%, var(--paper-shade));
    border-top: 12px solid var(--pool-deep);
  }
  .letterhead .wordmark { margin-top: 30px; }
  .letterhead-email {
    text-align: center; margin-top: 14px;
    font-size: 10.5px; letter-spacing: 2px; color: var(--ink-grey);
  }

  /* Envelope */
  .envelope {
    left: 742px; top: 548px; width: 263px; height: 209px;
    background: linear-gradient(180deg, var(--paper) 45%, var(--paper-shade));
    border-top: 12px solid var(--pool-deep);
  }
  .envelope .wordmark { position: absolute; left: 18px; top: 22px; text-align: left; }

  /* Business card – front */
  .card-front {
    left: 560px; top: 650px; width: 197px; height: 158px;
    background: var(--pool);
    display: flex; align-items: center; justify-content: center;
  }
  .card-front .wordmark { color: var(--beige); }

  /* Business card – back */
  .card-back {
    left: 757px; top: 690px; width: 246px; height: 160px;
    background: var(--paper);
    color: var(--text-dark);
  }
  .card-title {
    position: absolute; left: 10px; top: 22px;
    font-size: 17px; color: var(--ink-grey); white-space: nowrap; line-height: 1;
  }
  .card-title small { font-size: 9px; letter-spacing: 1px; margin-left: 3px; }
  .card-band {
    position: absolute; left: 0; top: 52px; width: 100%; height: 12px;
    background: var(--pool);
    color: var(--paper); font-size: 7.4px; letter-spacing: 1px; line-height: 12px;
    padding-left: 6px; white-space: nowrap; overflow: hidden;
  }
  .card-details { position: absolute; left: 8px; top: 88px; font-size: 5px; line-height: 1.45; }
  .card-details dt { color: var(--text-blue); font-size: 5.5px; margin-top: 4px; }
  .card-details dt:first-child { margin-top: 0; }
  .card-person { position: absolute; right: 8px; top: 78px; text-align: right; color: var(--text-blue); line-height: 1.1; }
  .card-person .person-name { font-size: 10px; }
  .card-person .person-role { font-size: 6px; margin-top: 2px; }

  /* Colour swatches */
  .swatch { left: 1013px; width: 155px; height: 124px; background: var(--paper); }
  .swatch .chip { height: 80px; }
  .swatch p { font-family: Arial, Helvetica, sans-serif; font-size: 13px; color: #111; line-height: 16px; padding: 4px 2px; }
  .swatch-beige { top: 51px; }
  .swatch-beige .chip { background: var(--beige); }
  .swatch-pool { top: 197px; }
  .swatch-pool .chip { background: var(--pool); }
</style>
</head>
<body>

  <section class="piece folder" aria-label="Presentation folder">
    <div class="folder-label">
      <div class="wordmark"><span class="name">Brackenridge</span><span class="sub">DESIGN STUDIO</span></div>
    </div>
    <div class="folder-dots"><span></span><span></span><span></span><span></span><span></span></div>
  </section>

  <section class="piece letterhead" aria-label="Letterhead">
    <div class="wordmark small"><span class="name">Brackenridge</span><span class="sub">DESIGN STUDIO</span></div>
    <p class="letterhead-email">harriet@brackenridgedesignstudio.example.au</p>
  </section>

  <section class="piece envelope" aria-label="Envelope">
    <div class="wordmark small"><span class="name">Brackenridge</span><span class="sub">DESIGN STUDIO</span></div>
  </section>

  <section class="piece card-front" aria-label="Business card front">
    <div class="wordmark small"><span class="name">Brackenridge</span><span class="sub">DESIGN STUDIO</span></div>
  </section>

  <section class="piece card-back" aria-label="Business card back">
    <p class="card-title">Brackenridge<small>DESIGN STUDIO</small></p>
    <p class="card-band">harriet@brackenridgedesignstudio.example.au</p>
    <div class="card-person">
      <p class="person-name">Harriet Oakley</p>
      <p class="person-role">Bachelor of Architecture</p>
    </div>
    <dl class="card-details">
      <dt>WEB</dt><dd>brackenridgedesignstudio.example.au</dd>
      <dt>TELEPHONE</dt><dd>0497 283 541</dd>
      <dt>ADDRESS</dt><dd>14 Pembury Road<br>Larkmoor East VIC 3999</dd>
    </dl>
  </section>

  <figure class="piece swatch swatch-beige">
    <div class="chip"></div>
    <p>S11A2<br>Soft Beige</p>
  </figure>
  <figure class="piece swatch swatch-pool">
    <div class="chip"></div>
    <p>S35B2<br>Still Lagoon</p>
  </figure>

</body>
</html>
```